Web Design Project

My site is already up - www.brightwell-hub.com but is very basic at this stage.
I need a to make the design look better and lift it a bit.
I have my own ideas about what I want.
The target market for the site is women - mainly professional, corporate women around the world aged between 28-40 yrs or thereabouts.
There are 3 main areas the site will focus on:
1: Blog and Inbox magazine with contributing writers on various topics from food, diet, emotional intelligence, intuition, feminine energy sexual and non, money to name a few.
2. There is an Ebook that is being added to the site later this year taking a deeper look at all of these topics. For now those subscribing get a free summary of the book.
Book called "Marigold - Your Gentle Guide to a Calmer Rhythm"
Happy to use the title for the FREE summary for subscribers.
3. Events / retreats. We are kicking off with our first Brightwell-hub retreat in Bali in late Oct 2012. We have amazing shots of the villa we will use and the activities etc that will make up a part of the retreat.
Yoga & meditation
Surfing
Photography
Keen to see what you all come up with.
NOTE: I dont want anything too busy. Keep it fairly clean, simple and in keeping with the general look and feel right now.
Updates
Target Market(s)
Look and feel
Each slider illustrates characteristics of the customer's brand and the style your logo design should communicate.

```html
<!DOCTYPE html>
<html lang="en">
<head>
<meta charset="utf-8">
<title>Brightwell-hub.com</title>
<link rel="stylesheet" href="https://fonts.googleapis.com/css2?family=Ubuntu:wght@300;400;500&family=Open+Sans:ital,wght@0,400;0,600;1,400;1,600&display=swap">
<style>
:root{
  --orange:#fba31a;
  --orange-light:#ffbe3a;
  --yellow:#ffc81f;
  --yellow-deep:#fbb50e;
  --white:#ffffff;
  --ink:#222222;
  --text:#555555;
  --muted:#666666;
  --accent:#f29a00;
  --btn:#e6e6e6;
  --btn-dark:#2b2b2b;
  --line:#bdbdbd;
  --photo-a:#f3ece6;
  --photo-b:#c98a66;
}
*{margin:0;padding:0;box-sizing:border-box}
html,body{width:1200px;height:1088px;overflow:hidden;background:var(--white)}
body{position:relative;font-family:"Open Sans",sans-serif;color:var(--text)}
.site-header{position:absolute;left:0;top:0;width:1200px;height:130px;background:linear-gradient(180deg,var(--orange-light),var(--orange))}
.brand{position:absolute;left:41px;top:46px;font-family:"Ubuntu",sans-serif;font-weight:500;font-size:38px;color:var(--white);letter-spacing:.5px}
.main-nav{position:absolute;left:515px;top:67px;display:flex;align-items:center;height:36px}
.main-nav a{font-family:"Ubuntu",sans-serif;font-size:18px;color:var(--white);text-decoration:none;padding:0 24px;line-height:36px;position:relative}
.main-nav a+a::before{content:"";position:absolute;left:0;top:-6px;height:50px;border-left:1px solid rgba(255,255,255,.45)}
.main-nav a.current{background:var(--white);color:var(--ink);border-radius:18px;padding:0 22px;margin-right:3px}
.main-nav a.current+a::before{display:none}
.hero{position:absolute;left:0;top:130px;width:1200px;height:440px;background:linear-gradient(180deg,var(--yellow),var(--yellow-deep))}
.hero-card{position:absolute;left:24px;top:19px;width:1146px;height:400px;background:var(--white);border-radius:10px;overflow:hidden}
.hero-card::after{content:"";position:absolute;left:10px;right:10px;bottom:10px;height:50px;background:linear-gradient(180deg,rgba(240,240,240,0),#ededed);border-radius:0 0 6px 6px}
.hero-photo{position:absolute;left:516px;top:10px;width:590px;height:380px;background:radial-gradient(ellipse at 60% 55%,var(--photo-b) 0%,#e4c7b4 35%,var(--photo-a) 70%,var(--white) 100%);z-index:1}
.hero-copy{position:absolute;left:59px;top:60px;width:440px;z-index:2}
.hero-copy h1{font-family:"Ubuntu",sans-serif;font-weight:300;font-size:36px;line-height:44px;color:#333}
.hero-copy .quote-by{font-family:"Ubuntu",sans-serif;font-weight:300;font-size:18px;color:var(--muted);margin-top:6px}
.hero-copy p{font-size:13px;line-height:21px;color:#333;margin-top:12px;padding-left:4px}
.hero-actions{display:flex;gap:13px;margin-top:21px}
.btn{font-family:"Ubuntu",sans-serif;font-size:20px;font-weight:300;height:39px;line-height:39px;padding:0 22px;border-radius:5px;display:inline-flex;align-items:center;gap:8px}
.btn-dark{background:var(--btn-dark);color:var(--white)}
.btn-light{background:var(--btn);color:#444}
.slider-dots{position:absolute;left:28px;top:360px;display:flex;gap:5px;z-index:2}
.slider-dots span{width:13px;height:13px;border-radius:50%;background:#d8d8d8}
.slider-dots span.active{background:#111}
.content{position:absolute;left:0;top:570px;width:1200px;height:435px;background:linear-gradient(180deg,var(--white),#f0f0f0)}
.column{position:absolute;top:30px;width:350px}
.col-blog{left:38px}.col-ebook{left:427px}.col-events{left:806px}
.column h2{font-family:"Ubuntu",sans-serif;font-weight:400;font-size:24px;color:var(--ink);margin-bottom:12px}
.column p{font-style:italic;font-size:12.5px;line-height:21px;color:var(--muted)}
.byline{font-family:"Ubuntu",sans-serif;font-size:14.5px;color:#444;margin:6px 0 30px;text-transform:uppercase}
.ebook-title{font-family:"Ubuntu",sans-serif;font-size:18px;color:var(--ink)}
.ebook-sub{font-style:italic;font-size:12.5px;color:#333;margin-bottom:16px}
.col-ebook p+p{margin-top:6px}
.event{display:flex;gap:12px;margin-bottom:26px}
.event-photo{flex:0 0 102px;height:82px;border:3px solid var(--white);box-shadow:0 1px 3px rgba(0,0,0,.25);background:linear-gradient(135deg,#b89878,#d9c2a8 55%,#8a7058)}
.event-photo.alt{background:linear-gradient(135deg,#cdb48a,#efe2c6 55%,#a08466)}
.event h3{font-family:"Ubuntu",sans-serif;font-weight:400;font-size:16px;color:#333}
.read-more{font-style:italic;font-weight:600;font-size:12.5px;color:var(--accent);display:block;margin-top:4px;padding-left:3px}
.divider{position:absolute;top:35px;height:323px;border-left:1px dotted #888}
.view-more{position:absolute;top:350px;height:31px;width:122px;background:var(--btn);border-radius:4px;font-family:"Ubuntu",sans-serif;font-size:14.5px;color:#222;display:flex;align-items:center;justify-content:center;gap:6px}
.site-footer{position:absolute;left:0;top:1005px;width:1200px;height:83px;background:var(--white)}
.copyright{position:absolute;left:23px;top:15px;font-size:13px;color:var(--muted)}
.footer-nav{position:absolute;right:243px;top:17px;font-size:13px;color:#444}
.footer-nav a{color:#444;text-decoration:none}
.footer-nav .sep{margin:0 11px}
</style>
</head>
<body>
<header class="site-header">
  <div class="brand">Brightwell-hub.com</div>
  <nav class="main-nav">
    <a class="current">Home</a><a>About Us</a><a>Blog</a><a>Community</a><a>Retreats</a><a>Contact</a>
  </nav>
</header>

<section class="hero">
  <div class="hero-card">
    <div class="hero-photo" role="img" aria-label="Smiling woman in a white shirt pointing upward"></div>
    <div class="hero-copy">
      <h1>The western Woman Will<br>Change the World</h1>
      <div class="quote-by">Amara Quinn</div>
      <p>To be the best we know what and how to present beautifully the working of the client's need and their advantages be highlighted.<br>We act in accordance with the Industry</p>
      <div class="hero-actions">
        <span class="btn btn-dark">Subscribe <svg width="8" height="14" viewBox="0 0 8 14"><path d="M1 1l6 6-6 6" fill="none" stroke="currentColor" stroke-width="1.6"/></svg></span>
        <span class="btn btn-light">learn more <svg width="8" height="14" viewBox="0 0 8 14"><path d="M1 1l6 6-6 6" fill="none" stroke="currentColor" stroke-width="1.6"/></svg></span>
      </div>
    </div>
    <div class="slider-dots"><span class="active"></span><span></span><span></span><span></span><span></span></div>
  </div>
</section>

<main class="content">
  <section class="column col-blog">
    <h2>Recent Blog</h2>
    <p>We at Lumacraft Studio think graphic design as a combination and collaboration of ideas and technology. Our Website Design team give an unforgettable</p>
    <div class="byline">By Author Name</div>
    <p>Lumacraft Studio provides you the Search Engine Optimization making your website search engine friendly. So that the website can achieve top position and ranking in the Internet searches and thereby increasing the scope for the website to be found by customers.</p>
    <div class="byline">By Author Name</div>
  </section>
  <div class="divider" style="left:396px"></div>
  <section class="column col-ebook">
    <h2>Ebook</h2>
    <div class="ebook-title">Marigold</div>
    <div class="ebook-sub">Your Gentle Guide to a Calmer Rhythm</div>
    <p>E-Commerce is a major progress in technology that has changed the way in which the customers now purchase information, products and the services.</p>
    <p>Lumacraft Studio is specialized in handling advanced web projects and the ongoing projects that require permanent maintenance and support. We like challenges and do complete these challenge with expertise we like solving questions that arises in such projects as these helps us to grow also.</p>
  </section>
  <div class="divider" style="left:778px"></div>
  <section class="column col-events">
    <h2>Events &amp; Retreats</h2>
    <div class="event">
      <div class="event-photo" role="img" aria-label="Two women smiling together"></div>
      <div><h3>Event Name here</h3><p>We at Lumacraft Studio think graphic design as a combination and collaboration of ideas and technology.</p><span class="read-more">read more..</span></div>
    </div>
    <div class="event">
      <div class="event-photo alt" role="img" aria-label="Woman speaking at a microphone"></div>
      <div><h3>Event Name here</h3><p>We like challenges and do complete these challenge with expertise we like solving questions that arises in such projects as these helps us to grow also.</p><span class="read-more">read more..</span></div>
    </div>
  </section>
  <span class="view-more" style="left:31px">VIEW MORE <svg width="6" height="10" viewBox="0 0 6 10"><path d="M1 1l4 4-4 4" fill="none" stroke="currentColor" stroke-width="1.4"/></svg></span>
  <span class="view-more" style="left:425px">VIEW MORE <svg width="6" height="10" viewBox="0 0 6 10"><path d="M1 1l4 4-4 4" fill="none" stroke="currentColor" stroke-width="1.4"/></svg></span>
  <span class="view-more" style="left:812px">VIEW MORE <svg width="6" height="10" viewBox="0 0 6 10"><path d="M1 1l4 4-4 4" fill="none" stroke="currentColor" stroke-width="1.4"/></svg></span>
</main>

<footer class="site-footer">
  <div class="copyright">Copyright ©2012 brightwell-hub.com</div>
  <nav class="footer-nav">
    <a>Home</a><span class="sep">|</span><a>About Us</a><span class="sep">|</span><a>Blog</a><span class="sep">|</span><a>Community</a><span class="sep">|</span><a>Retreats</a><span class="sep">|</span><a>Contact</a>
  </nav>
</footer>
</body>
</html>
```